Business Card Design Project

Business Card design based on logo.

I need business card, letterhead, envelope, and if possible, Powerpoint slide template.

On front of business card: Just logo- and  my name and title:  Helena Marsk, Principal

On reverse-logo and the rest of the contact info:

4871 Orchard Lane
Davis, CA 95618
650-318-2274
hm@brevicaeducation.example

On letterhead-Just logo at top, at bottom  the rest-very small along the bottom

On PPT slide-just the logo.

I also want to try a few other colors-I like lime/dark grey (not black) but would like to try Sienna, maybe also indigo or bright blue-green.

I forgot to add-

On the business card-switch to vertical on reverse side and put:

Reverse side-switch to vertical and list:

Helena Marsk
Principal
Brevica Tutoring Partners, LLC

650-318-2274

4871 Orchard Lane
Davis, CA 95618

Helena Marsk
Principal

650-318-2274

4871 Orchard Lane
Davis, CA 95618

I have another project at the same time-for Stationery. Feel free to submit to that one also.

That one includes letterhead, envelope, PPT slide, folder cover sheet-HM

Industry/Entity Type

Business

Requirements
Must have
• Must use logo-preferably lime green version-with gray, not black or just 2-tone -logo on colored background.

```html
<!DOCTYPE html>
<html lang="en">
<head>
<meta charset="utf-8">
<title>Brevica Tutoring – Business Cards</title>
<link rel="stylesheet" href="https://fonts.googleapis.com/css2?family=Libre+Baskerville&family=Arimo:wght@400;700&family=Jost:wght@400&display=swap">
<style>
  :root {
    --lime: #8cb43f;
    --lime-tint: #f4f6ee;
    --charcoal: #4a4a4a;
    --ink: #333333;
    --paper: #ffffff;
    --backdrop: #ebe8e3;
    --serif: "Libre Baskerville", Georgia, serif;
    --sans: "Arimo", Arial, sans-serif;
    --geo: "Jost", "Futura", sans-serif;
  }
  * { box-sizing: border-box; margin: 0; padding: 0; }
  html, body { width: 1200px; height: 713px; overflow: hidden; }
  body { background: var(--backdrop); position: relative; font-family: var(--sans); }

  .card {
    position: absolute;
    width: 497px;
    height: 283px;
    background: var(--paper);
    box-shadow: 0 2px 6px rgba(0,0,0,.18);
    overflow: hidden;
  }
  .card--contact { left: 84px;  top: 54px; }
  .card--green   { left: 616px; top: 59px; background: var(--lime); }
  .card--pattern { left: 87px;  top: 371px; }
  .card--plain   { left: 617px; top: 375px; }

  .top-stripe { position: absolute; left: 0; top: 0; width: 100%; height: 11px; background: var(--lime); }

  .pattern-field {
    position: absolute; inset: 0 0 50px 0;
    background: linear-gradient(180deg, var(--lime-tint), #f8f9f4);
  }

  .brand {
    position: absolute; left: 0; width: 100%;
    display: flex; flex-direction: column; align-items: center;
    color: var(--charcoal);
    font-family: var(--serif);
    text-transform: uppercase;
    line-height: 1;
  }
  .brand__mark { width: 38px; height: 38px; background: var(--lime); margin-bottom: 16px; }
  .brand__name { font-size: 34px; letter-spacing: 6px; text-align: center; }
  .brand__name span { display: block; font-size: 18px; letter-spacing: 8px; margin-top: 8px; }

  .card--contact .brand { top: 24px; }
  .card--contact .brand__mark { width: 34px; height: 34px; margin-bottom: 14px; }
  .card--contact .brand__name { font-size: 30px; }
  .card--contact .brand__name span { font-size: 16px; }

  .card--green .brand { top: 74px; color: var(--paper); }
  .card--green .brand__mark { background: var(--paper); width: 46px; height: 46px; }

  .card--pattern .brand { top: 86px; }
  .card--pattern .brand__name { font-size: 58px; letter-spacing: 10px; }
  .card--pattern .brand__name span { font-size: 30px; letter-spacing: 12px; margin-top: 12px; }

  .card--plain .brand { top: 58px; }

  .web {
    position: absolute; left: 0; bottom: 16px; width: 100%;
    text-align: center;
    font-family: var(--geo);
    font-size: 20px; letter-spacing: 2.4px;
    color: var(--ink);
  }
  .card--green .web { color: var(--paper); }

  .person {
    position: absolute; right: 280px; top: 192px;
    text-align: right; color: var(--ink);
    font-size: 13px; line-height: 19px;
  }
  .person__name { color: var(--lime); font-weight: 700; font-size: 18px; line-height: 22px; }

  .divider { position: absolute; left: 231px; top: 190px; width: 1px; height: 80px; background: #bdbdbd; }

  .contact-list {
    position: absolute; left: 244px; top: 195px;
    list-style: none; color: var(--ink);
    font-size: 13px; line-height: 19px;
  }
  .contact-list li { display: flex; align-items: center; gap: 6px; }
  .contact-list svg { width: 10px; height: 10px; fill: var(--ink); flex: none; }
</style>
</head>
<body>

  <section class="card card--contact">
    <div class="top-stripe"></div>
    <div class="brand">
      <div class="brand__mark"></div>
      <div class="brand__name">Brevica<span>Tutoring</span></div>
    </div>
    <div class="person">
      <p class="person__name">Your Name</p>
      <p>Title</p>
      <p>00, Complex name</p>
      <p>City, State 0042</p>
    </div>
    <div class="divider"></div>
    <ul class="contact-list">
      <li><svg viewBox="0 0 10 10"><path d="M2 0.5l2 2-1 1.2c.6 1.3 1.5 2.2 2.8 2.8l1.2-1 2 2-1.3 1.8C4 9 1 6 .3 1.8z"/></svg>0987 654321</li>
      <li><svg viewBox="0 0 10 10"><path d="M1 4h8v4H1z M2.5 1h5l1.5 3h-8z"/></svg>0987 654321</li>
      <li><svg viewBox="0 0 10 10"><path d="M0.5 2h9v6h-9z M0.5 2l4.5 3.5L9.5 2" stroke="#fff" stroke-width=".8"/></svg>info@brevicatutoring.example</li>
      <li><svg viewBox="0 0 10 10"><circle cx="5" cy="5" r="4.5"/><path d="M0.5 5h9M5 0.5c-2 2.5-2 6.5 0 9M5 0.5c2 2.5 2 6.5 0 9" stroke="#fff" stroke-width=".7" fill="none"/></svg>www.brevicatutoring.example</li>
    </ul>
  </section>

  <section class="card card--green">
    <div class="brand">
      <div class="brand__mark"></div>
      <div class="brand__name">Brevica<span>Tutoring</span></div>
    </div>
    <p class="web">www.brevicatutoring.example</p>
  </section>

  <section class="card card--pattern">
    <div class="pattern-field" role="img" aria-label="Faint repeating brand pattern in pale lime"></div>
    <div class="brand">
      <div class="brand__name">Brevica<span>Tutoring</span></div>
    </div>
    <p class="web">www.brevicatutoring.example</p>
  </section>

  <section class="card card--plain">
    <div class="brand">
      <div class="brand__mark"></div>
      <div class="brand__name">Brevica<span>Tutoring</span></div>
    </div>
    <p class="web">www.brevicatutoring.example</p>
  </section>

</body>
</html>
```